I'm looking for a smart new design for business cards

Industry/Entity Type

Commercial Electrical

Contact Information for Business Card

Logo, name, email, position, website QR

Requirements
Nice to have
• Logo embedded behind the text side

```html
<!DOCTYPE html>
<html lang="en">
<head>
<meta charset="utf-8">
<title>Voltara Commercial Electrical – Business Card</title>
<link rel="stylesheet" href="https://fonts.googleapis.com/css2?family=Montserrat:wght@700;800&family=Roboto:wght@400&display=swap">
<style>
  :root {
    --navy: #0b0f82;
    --red: #e0002a;
    --ink: #111111;
    --grey-text: #555555;
    --rule: #cfcfcf;
    --paper: #ffffff;
    --backdrop: #e4e4e4;
  }
  * { box-sizing: border-box; margin: 0; padding: 0; }
  html, body { width: 1200px; height: 1200px; overflow: hidden; }
  body {
    background: var(--backdrop);
    position: relative;
    font-family: "Roboto", Arial, sans-serif;
  }
  .card {
    position: absolute;
    left: 256px;
    width: 688px;
    height: 393px;
    border-radius: 18px;
    overflow: hidden;
  }
  .card--front { top: 159px; background: var(--paper); }
  .card--back { top: 654px; background: var(--navy); }

  /* Front brand block */
  .brand {
    position: absolute;
    text-align: center;
    font-family: "Montserrat", Arial, sans-serif;
    font-weight: 800;
    text-transform: uppercase;
  }
  .brand__mark {
    display: flex;
    align-items: center;
    justify-content: center;
    gap: 14px;
  }
  .brand__square { display: inline-block; background: var(--red); }
  .brand--front { left: 330px; width: 320px; top: 50px; color: var(--navy); }
  .brand--front .brand__word { font-size: 66px; letter-spacing: 1px; line-height: 1; }
  .brand--front .brand__square { width: 30px; height: 30px; }
  .brand--front .brand__line { font-size: 19px; line-height: 25px; margin-top: 20px; letter-spacing: 0.3px; }

  .brand--back { left: 0; width: 100%; top: 88px; color: #ffffff; }
  .brand--back .brand__word { font-size: 100px; letter-spacing: 2px; line-height: 1; }
  .brand--back .brand__square { width: 44px; height: 44px; }
  .brand--back .brand__line { font-size: 26px; line-height: 34px; margin-top: 34px; letter-spacing: 0.5px; }

  /* Person */
  .person { position: absolute; left: 48px; top: 244px; }
  .person__name {
    font-family: "Montserrat", Arial, sans-serif;
    font-weight: 800;
    font-size: 25px;
    color: var(--navy);
    letter-spacing: 0.3px;
    line-height: 1;
  }
  .person__role { font-size: 15px; color: var(--grey-text); margin-top: 5px; }

  .divider {
    position: absolute;
    left: 48px; top: 303px;
    width: 591px; height: 1px;
    background: var(--rule);
  }

  .contact-list {
    position: absolute;
    left: 45px; top: 312px;
    list-style: none;
    font-size: 15.5px;
    color: var(--grey-text);
  }
  .contact-list li { display: flex; align-items: center; height: 20.5px; }
  .contact-list svg { width: 14px; height: 14px; margin-right: 9px; fill: var(--red); }

  .address {
    position: absolute;
    right: 43px; top: 315px;
    text-align: right;
    font-size: 15.5px;
    line-height: 21px;
    color: var(--grey-text);
    font-style: normal;
  }
</style>
</head>
<body>

<section class="card card--front">
  <div class="brand brand--front">
    <div class="brand__mark">
      <span class="brand__word">Voltara</span>
      <span class="brand__square"></span>
    </div>
    <div class="brand__line">Commercial Electrical</div>
  </div>

  <div class="person">
    <h1 class="person__name">DANIEL HARPER</h1>
    <p class="person__role">President</p>
  </div>

  <div class="divider"></div>

  <ul class="contact-list">
    <li>
      <svg viewBox="0 0 24 24" aria-hidden="true"><path d="M6.6 10.8a15.2 15.2 0 0 0 6.6 6.6l2.2-2.2a1 1 0 0 1 1-.25 11.4 11.4 0 0 0 3.6.57 1 1 0 0 1 1 1V20a1 1 0 0 1-1 1A17 17 0 0 1 3 4a1 1 0 0 1 1-1h3.5a1 1 0 0 1 1 1c0 1.25.2 2.45.57 3.57a1 1 0 0 1-.25 1z"/></svg>
      555-210-4837
    </li>
    <li>
      <svg viewBox="0 0 24 24" aria-hidden="true"><path d="M7 1h10a2 2 0 0 1 2 2v18a2 2 0 0 1-2 2H7a2 2 0 0 1-2-2V3a2 2 0 0 1 2-2zm0 3v14h10V4zm5 15.2a1.1 1.1 0 1 0 0 2.2 1.1 1.1 0 0 0 0-2.2z"/></svg>
      555-318-2096
    </li>
    <li>
      <svg viewBox="0 0 24 24" aria-hidden="true"><path d="M2 5h20v14H2zm2 2v.4l8 5.3 8-5.3V7zm0 2.8V17h16V9.8l-8 5.3z"/></svg>
      info@voltara.com
    </li>
  </ul>

  <address class="address">
    412 Harbour Street<br>
    Millbrook, Canada 48210<br>
    www.voltara.com
  </address>
</section>

<section class="card card--back">
  <div class="brand brand--back">
    <div class="brand__mark">
      <span class="brand__word">Voltara</span>
      <span class="brand__square"></span>
    </div>
    <div class="brand__line">Commercial Electrical</div>
  </div>
</section>

</body>
</html>
```